App Icon Designs

I am creating an app and I need icons for these categories:
Education
Entertainment
Finance
Games
Health & Fitness
Kids
Lifestyle
Medical
Music
Navigation
News
Photo & Video
Social Networking
Sports
Travel
Utilities
Weather
I would like the icon designs to imitate the style of the included picture. I have also included a picture of the buttons the icons should fit in (75 x 75 pixels). The icons should stick the the simple and flat look.
Please keep all icons 75 x 75 pixels, and NOT 90 x 90 pixels.
Prize increased to $230. Please do your best work. If anyone can successfully imitate the design of the picture included, I will be glad to increase the prize by another $100.

```html
<!DOCTYPE html>
<html lang="en">
<head>
<meta charset="utf-8">
<title>Discover Categories</title>
<link href="https://fonts.googleapis.com/css2?family=Montserrat:wght@400&display=swap" rel="stylesheet">
<style>
  :root {
    --canvas-bg: #ebe8e4;
    --entertainment: #34495e;
    --finance: #00c08b;
    --games: #ff85e0;
    --medical: #ff5a63;
    --music: #ffcb2f;
    --navigation: #33cdc0;
    --social: #ff7a45;
    --sports: #3498db;
    --label: #ffffff;
    --edge-shadow: rgba(0, 0, 0, 0.13);
    --long-shadow: rgba(0, 0, 0, 0.10);
  }
  html, body {
    margin: 0;
    padding: 0;
    overflow: hidden;
  }
  .canvas {
    position: relative;
    width: 1200px;
    height: 1000px;
    background: var(--canvas-bg);
    overflow: hidden;
  }
  .category-list {
    position: absolute;
    left: 87px;
    top: 95px;
    width: 498px;
    margin: 0;
    padding: 0;
    list-style: none;
  }
  .category {
    position: relative;
    height: 90px;
    margin-bottom: 11px;
    border-radius: 6px;
    overflow: hidden;
    box-shadow: 3px 3px 0 var(--edge-shadow);
  }
  .category__icon {
    position: absolute;
    left: 0;
    top: 0;
    width: 130px;
    height: 90px;
  }
  .category__label {
    position: absolute;
    left: 143px;
    top: 0;
    line-height: 90px;
    font-family: "Montserrat", sans-serif;
    font-weight: 400;
    font-size: 34px;
    color: var(--label);
    letter-spacing: 0.3px;
  }
  .category--entertainment { background: var(--entertainment); }
  .category--finance { background: var(--finance); }
  .category--games { background: var(--games); }
  .category--medical { background: var(--medical); }
  .category--music { background: var(--music); }
  .category--navigation { background: var(--navigation); }
  .category--social { background: var(--social); }
  .category--sports { background: var(--sports); }
  .long-shadow { fill: var(--long-shadow); }
</style>
</head>
<body>
<div class="canvas">
  <ul class="category-list">
    <li class="category category--entertainment">
      <svg class="category__icon" viewBox="0 0 130 90" aria-hidden="true">
        <polygon class="long-shadow" points="41,24 83,66 -17,166 -59,124"/>
        <g class="popcorn">
          <circle cx="50" cy="30" r="8" fill="#fff3d6"/>
          <circle cx="62" cy="25" r="9" fill="#fff8e6"/>
          <circle cx="74" cy="30" r="8" fill="#fff3d6"/>
          <circle cx="56" cy="33" r="7" fill="#ffe9b8"/>
          <circle cx="69" cy="34" r="7" fill="#ffe9b8"/>
          <polygon points="45,36 79,36 74,74 50,74" fill="#ffffff"/>
          <polygon points="45,36 51,36 53,74 50,74" fill="#e53935"/>
          <polygon points="57,36 63,36 62.5,74 57.5,74" fill="#e53935"/>
          <polygon points="69,36 75,36 72.5,74 69.5,74" fill="#e53935"/>
        </g>
      </svg>
      <span class="category__label">entertainment</span>
    </li>
    <li class="category category--finance">
      <svg class="category__icon" viewBox="0 0 130 90" aria-hidden="true">
        <polygon class="long-shadow" points="41,24 83,66 -17,166 -59,124"/>
        <circle cx="62" cy="45" r="30" fill="#f2a900"/>
        <circle cx="62" cy="45" r="24" fill="#ffc928"/>
        <text x="62" y="57" text-anchor="middle" font-family="Montserrat, sans-serif" font-size="34" fill="#e39a00">$</text>
      </svg>
      <span class="category__label">finance</span>
    </li>
    <li class="category category--games">
      <svg class="category__icon" viewBox="0 0 130 90" aria-hidden="true">
        <polygon class="long-shadow" points="41,24 83,66 -17,166 -59,124"/>
        <path d="M40 34 Q44 28 54 29 L70 29 Q80 28 84 34 Q92 50 89 60 Q86 66 79 61 L72 54 L52 54 L45 61 Q38 66 35 60 Q32 50 40 34 Z" fill="#ffffff"/>
        <rect x="46" y="39" width="4" height="12" fill="#555"/>
        <rect x="42" y="43" width="12" height="4" fill="#555"/>
        <circle cx="74" cy="38" r="2.6" fill="#2ecc71"/>
        <circle cx="79" cy="43" r="2.6" fill="#e74c3c"/>
        <circle cx="69" cy="43" r="2.6" fill="#3498db"/>
        <circle cx="74" cy="48" r="2.6" fill="#f1c40f"/>
      </svg>
      <span class="category__label">games</span>
    </li>
    <li class="category category--medical">
      <svg class="category__icon" viewBox="0 0 130 90" aria-hidden="true">
        <polygon class="long-shadow" points="41,24 83,66 -17,166 -59,124"/>
        <path d="M55 24 h14 v14 h14 v14 h-14 v14 h-14 v-14 h-14 v-14 h14 z" fill="#e0e0e0"/>
        <path d="M54 23 h14 v14 h14 v14 h-14 v14 h-14 v-14 h-14 v-14 h14 z" fill="#ffffff"/>
      </svg>
      <span class="category__label">medical</span>
    </li>
    <li class="category category--music">
      <svg class="category__icon" viewBox="0 0 130 90" aria-hidden="true">
        <polygon class="long-shadow" points="41,24 83,66 -17,166 -59,124"/>
        <polygon points="50,28 82,20 82,30 54,37" fill="#b86fd6"/>
        <rect x="50" y="28" width="5" height="38" fill="#b86fd6"/>
        <rect x="77" y="20" width="5" height="38" fill="#b86fd6"/>
        <ellipse cx="45" cy="66" rx="10" ry="8" fill="#b86fd6"/>
        <ellipse cx="72" cy="58" rx="10" ry="8" fill="#b86fd6"/>
      </svg>
      <span class="category__label">music</span>
    </li>
    <li class="category category--navigation">
      <svg class="category__icon" viewBox="0 0 130 90" aria-hidden="true">
        <polygon class="long-shadow" points="41,24 83,66 -17,166 -59,124"/>
        <circle cx="62" cy="45" r="30" fill="#9aa0a6"/>
        <circle cx="62" cy="45" r="24" fill="#f4f4f4"/>
        <polygon points="75,32 65,48 59,42" fill="#e74c3c"/>
        <polygon points="49,58 59,42 65,48" fill="#7f8c8d"/>
        <circle cx="62" cy="45" r="2.5" fill="#555"/>
      </svg>
      <span class="category__label">navigation</span>
    </li>
    <li class="category category--social">
      <svg class="category__icon" viewBox="0 0 130 90" aria-hidden="true">
        <polygon class="long-shadow" points="41,24 83,66 -17,166 -59,124"/>
        <rect x="44" y="15" width="36" height="60" rx="5" fill="#ffffff"/>
        <rect x="47.5" y="23" width="29" height="44" fill="#3aa0e0"/>
        <circle cx="62" cy="71" r="2" fill="#cccccc"/>
      </svg>
      <span class="category__label">social networking</span>
    </li>
    <li class="category category--sports">
      <svg class="category__icon" viewBox="0 0 130 90" aria-hidden="true">
        <polygon class="long-shadow" points="41,24 83,66 -17,166 -59,124"/>
        <circle cx="62" cy="46" r="30" fill="#f47a3a"/>
        <g fill="none" stroke="#2c2c2c" stroke-width="3">
          <line x1="62" y1="16" x2="62" y2="76"/>
          <line x1="32" y1="46" x2="92" y2="46"/>
          <path d="M42 24 Q54 46 42 68"/>
          <path d="M82 24 Q70 46 82 68"/>
        </g>
      </svg>
      <span class="category__label">sports</span>
    </li>
  </ul>
</div>
</body>
</html>
```